Design a business card

I run a womens online boutique and would like a new business card as I have just re-branded and relaunched.

Something simple but yet eye catching. My Instagram page is @ambermistlineuk should you need to see the theme/colours/ products to give you inspiration. I have also attached the logos I use.

Thank you

```html
<!DOCTYPE html>
<html lang="en">
<head>
<meta charset="utf-8">
<title>Amber Mistline – Business Card</title>
<link rel="stylesheet" href="https://fonts.googleapis.com/css2?family=Cormorant+Garamond:wght@500&family=Open+Sans:wght@400;600&display=swap">
<style>
  :root {
    --backdrop: #e9e9ec;
    --gold: #b8953f;
    --gold-deep: #a8862f;
    --cream: #f4ecd4;
    --pale-gold: #dcc586;
    --ink-light: #ffffff;
    --card-shadow: rgba(60, 50, 30, 0.18);
  }
  * { margin: 0; padding: 0; box-sizing: border-box; }
  html, body { width: 1200px; height: 900px; overflow: hidden; }
  body {
    background: var(--backdrop);
    font-family: "Open Sans", Arial, sans-serif;
    color: var(--ink-light);
    position: relative;
  }
  .card {
    position: absolute;
    width: 500px;
    height: 290px;
    border-radius: 26px;
    background: var(--gold);
    overflow: hidden;
    box-shadow: 0 10px 28px var(--card-shadow);
  }
  /* Back of card */
  .card-back { left: 640px; top: 120px; }
  .brand {
    position: absolute;
    left: 0; right: 0; top: 92px;
    display: flex; align-items: center; justify-content: center; gap: 14px;
  }
  .brand-rule { width: 70px; height: 1.5px; background: var(--ink-light); }
  .brand-name {
    font-family: "Cormorant Garamond", Georgia, serif;
    font-weight: 500;
    font-size: 42px;
    letter-spacing: 1px;
    color: var(--ink-light);
  }
  .back-handle {
    position: absolute;
    left: 150px; top: 200px;
    display: flex; align-items: center; gap: 8px;
    font-size: 14px;
  }
  .dot-icon {
    width: 14px; height: 14px; border-radius: 50%;
    background: var(--ink-light);
    flex: none;
  }
  /* Front of card */
  .card-front { left: 80px; top: 480px; }
  .portrait {
    position: absolute; left: 0; top: 0;
    width: 260px; height: 290px;
    background:
      radial-gradient(ellipse at 30% 35%, var(--cream) 0%, var(--pale-gold) 55%, transparent 100%),
      linear-gradient(100deg, var(--cream) 0%, var(--pale-gold) 60%, var(--gold) 100%);
  }
  .holder {
    position: absolute;
    right: 34px; top: 68px;
    text-align: right;
  }
  .holder-name { font-size: 21px; letter-spacing: 1px; }
  .holder-rule { width: 120px; height: 1.5px; background: var(--ink-light); margin: 8px 0 6px auto; }
  .holder-role { font-size: 15px; letter-spacing: 0.5px; }
  .contacts {
    position: absolute;
    right: 34px; bottom: 30px;
    display: flex; flex-direction: column; align-items: flex-end; gap: 9px;
    font-size: 13.5px;
  }
  .contact-row { display: flex; align-items: center; gap: 16px; }
  .contact-item { display: flex; align-items: center; gap: 7px; }
  .contact-item svg { width: 15px; height: 15px; flex: none; }
</style>
</head>
<body>

  <section class="card card-back" aria-label="Card back">
    <div class="brand">
      <span class="brand-rule"></span>
      <span class="brand-name">Amber Mistline</span>
    </div>
    <div class="back-handle">
      <span class="dot-icon"></span>
      <span>@ambermistlineuk</span>
    </div>
  </section>

  <section class="card card-front" aria-label="Card front">
    <div class="portrait" role="img" aria-label="Fashion portrait of a woman with platinum hair dissolving into gold dust"></div>

    <div class="holder">
      <div class="holder-name">Rosalie Hart</div>
      <div class="holder-rule"></div>
      <div class="holder-role">Owner</div>
    </div>

    <div class="contacts">
      <div class="contact-row">
        <span class="contact-item"><span class="dot-icon"></span>@ambermistlineuk</span>
        <span class="contact-item">
          <svg viewBox="0 0 24 24" aria-hidden="true"><path fill="#ffffff" d="M6.6 10.8a15.1 15.1 0 0 0 6.6 6.6l2.2-2.2a1 1 0 0 1 1-.25 11.4 11.4 0 0 0 3.6.57 1 1 0 0 1 1 1V20a1 1 0 0 1-1 1A17 17 0 0 1 3 4a1 1 0 0 1 1-1h3.5a1 1 0 0 1 1 1c0 1.25.2 2.45.57 3.57a1 1 0 0 1-.25 1z"/></svg>
          +0198765432
        </span>
      </div>
      <div class="contact-row">
        <span class="contact-item">
          <svg viewBox="0 0 24 24" aria-hidden="true" fill="none" stroke="#ffffff" stroke-width="1.8"><circle cx="12" cy="12" r="9"/><ellipse cx="12" cy="12" rx="4" ry="9"/><path d="M3 12h18"/></svg>
          www.ambermistline.uk
        </span>
      </div>
    </div>
  </section>

</body>
</html>
```